Home Care company needs letter head branding

Home care company needs a letter head which can be used for all documents the company's clients view. We provided in home care for the elderly. We would like to use our company colors (2785A7, 0A4057 and 34A74D) and should not be too large as we will be using it on more than just a letter head but all documents our clients sign / receive.
Target Market(s)
Professional business
Industry/Entity Type
Health Care
Requirements
Must have
- corporate brand colors

```html
<!DOCTYPE html>
<html lang="en">
<head>
<meta charset="utf-8">
<title>Harbor Lane Home Health Letterhead</title>
<link rel="stylesheet" href="https://fonts.googleapis.com/css2?family=Lato:wght@400&family=Roboto:wght@400;500&display=swap">
<style>
  :root {
    --brand-blue: #2785A7;
    --brand-navy: #0A4057;
    --accent-lime: #A6C93A;
    --ink-grey: #7a7a7a;
    --ink-dark: #4a4a4a;
    --paper: #ffffff;
    --backdrop: #ececec;
  }
  html, body {
    margin: 0;
    padding: 0;
    width: 1200px;
    height: 866px;
    overflow: hidden;
    background: var(--backdrop);
  }
  .letterhead {
    position: absolute;
    left: 347px;
    top: 62px;
    width: 535px;
    height: 749px;
    background: var(--paper);
    overflow: hidden;
    font-family: "Roboto", sans-serif;
    color: var(--ink-grey);
  }
  .brand {
    position: absolute;
    left: 34px;
    top: 49px;
    display: flex;
    align-items: center;
    gap: 8px;
  }
  .brand-mark {
    width: 46px;
    height: 46px;
    border-radius: 50%;
    background: var(--brand-blue);
  }
  .brand-name {
    font-family: "Roboto", sans-serif;
    font-weight: 500;
    font-size: 19px;
    color: var(--brand-blue);
    white-space: nowrap;
  }
  .contact {
    position: absolute;
    left: 376px;
    top: 36px;
    font-family: "Lato", sans-serif;
    font-style: normal;
    font-size: 8.6px;
    line-height: 11.2px;
    color: var(--ink-dark);
  }
  .contact-address { margin: 0 0 5px; }
  .contact-row {
    display: flex;
    align-items: center;
    gap: 4px;
    height: 13.2px;
  }
  .contact-icon { width: 10px; height: 10px; flex: none; }
  .recipient {
    position: absolute;
    left: 44px;
    top: 196px;
    font-size: 9.6px;
    line-height: 14px;
    margin: 0;
  }
  .body-copy {
    position: absolute;
    left: 44px;
    top: 279px;
    width: 443px;
    font-size: 9.2px;
    line-height: 13.9px;
    text-align: justify;
  }
  .body-copy p { margin: 0 0 27.7px; }
  .signature {
    position: absolute;
    left: 43px;
    top: 476px;
    width: 102px;
    height: 68px;
    background: linear-gradient(135deg, #e3f0f5, #d2e7ef);
    border-radius: 4px;
  }
  .signatory-title {
    position: absolute;
    left: 43px;
    top: 558px;
    font-size: 9.6px;
    margin: 0;
  }
  .footer-rule {
    position: absolute;
    left: 0;
    right: 0;
    bottom: 46px;
    height: 5px;
    background: var(--accent-lime);
  }
  .footer-band {
    position: absolute;
    left: 0;
    right: 0;
    bottom: 0;
    height: 40px;
    background: var(--brand-blue);
  }
</style>
</head>
<body>
  <main class="letterhead">
    <header>
      <div class="brand">
        <span class="brand-mark" aria-hidden="true"></span>
        <span class="brand-name">Harbor Lane Home Health</span>
      </div>
      <address class="contact">
        <p class="contact-address">1280 Meadowbrook Ave, Suite 310<br>Riverton MD 20990</p>
        <div class="contact-row">
          <svg class="contact-icon" viewBox="0 0 12 12" aria-hidden="true">
            <circle cx="6" cy="6" r="6" fill="var(--brand-blue)"/>
            <path d="M4 3.2c.4-.3.8-.2 1 .2l.5 1c.1.3 0 .5-.2.7l-.3.3c.3.7.8 1.2 1.5 1.5l.3-.3c.2-.2.5-.3.7-.2l1 .5c.4.2.5.6.2 1l-.4.5c-.4.4-1.2.4-2.2-.2-1-.6-1.8-1.4-2.4-2.4-.6-1-.6-1.8-.2-2.2z" fill="#fff"/>
          </svg>
          <span>(301) 555-0147</span>
        </div>
        <div class="contact-row">
          <svg class="contact-icon" viewBox="0 0 12 12" aria-hidden="true">
            <circle cx="6" cy="6" r="6" fill="var(--brand-blue)"/>
            <rect x="3" y="4" width="6" height="4.2" rx="0.6" fill="#fff"/>
            <path d="M3.2 4.3 6 6.3l2.8-2" stroke="var(--brand-blue)" stroke-width="0.7" fill="none"/>
          </svg>
          <span>info@harborlanehealth.com</span>
        </div>
        <div class="contact-row">
          <svg class="contact-icon" viewBox="0 0 12 12" aria-hidden="true">
            <circle cx="6" cy="6" r="6" fill="var(--brand-blue)"/>
            <circle cx="6" cy="6" r="3.3" stroke="#fff" stroke-width="0.8" fill="none"/>
            <path d="M2.7 6h6.6M6 2.7c-1.4 1.8-1.4 4.8 0 6.6M6 2.7c1.4 1.8 1.4 4.8 0 6.6" stroke="#fff" stroke-width="0.7" fill="none"/>
          </svg>
          <span>www.harborlanehealth.com</span>
        </div>
      </address>
    </header>

    <p class="recipient">Dear Hallorin<br>Westbay Print Group<br>Department Design</p>

    <section class="body-copy">
      <p>Lorem ipsum dolor sit amet, consectetuer adipiscing elit. Aenean commodo ligula eget dolor. Aenean massa. Cum sociis natoque penatibus et magnis dis parturient montes, nascetur ridiculus mus. Donec quam felis, ultricies nec, pellentesque eu, pretium quis, sem. Nulla consequat massa quis enim. Donec pede justo, fringilla vel, aliquet nec, vulputate eget, arcu. In enim justo, rhoncus ut, imperdiet a, venenatis vitae, justo. Nullam dictum felis eu pede mollis pretium. Integer tincidunt. Cras dapibus. Vivamus elementum semper nisi.Nullam dictum felis eu pede mollis pretium. Integer tincidunt. Cras dapibus. Vivamus elementum semper nisi.felis eu pede mollis pretium. Integer tincidunt. Cras dapibus.</p>
      <p>Quisque rutrum. Aenean imperdiet. Etiam ultricies nisi vel augue. Curabitur ullamcorper ultricies nisi. Nam eget dui. Etiam rhoncus. Maecenas tempus, tellus eget condimentum rhoncus, sem quam semper libero, sit amet adipiscing sem neque sed ipsum.felis pede mollis pretium. I am tincidunt. Cras dapibus.</p>
    </section>

    <div class="signature" role="img" aria-label="Handwritten signature of the director"></div>
    <p class="signatory-title">Director/Excecutive Director</p>

    <footer>
      <div class="footer-rule" aria-hidden="true"></div>
      <div class="footer-band" aria-hidden="true"></div>
    </footer>
  </main>
</body>
</html>
```